Business Card & Stationary for Orthodontic Office
Lena Voss Orthodontics
Business Card & Stationary for Orthodontic Office  - Medical
Creative Brief
Professional
See Additional Comments
4127 Marlow Ct Williamsville, NY 14398
Info@SmileCraftClinics.com
www.SmileCraftClinics.com
The logo contains our DBA name however below should read smaller; Lena Voss D.M.D. M.S. PC Also the NCT attached should be included as well.
(additional locations) Blasdell 5193 Hollin Ridge Ave. Blasdell, NY 14387 (716)555-0193 Cheektowaga 2615 Fenwick Rd. Cheektowaga, NY 14391 (716)555-0147 Warsaw 58 Lorimer St. Warsaw, NY 14802 (585)555-0126 Attica 4712 W. Tarrow St. Attica, NY 14906 (585)555-0126
LVBrace LVBrace
*************EDIT TO BRIEF*************** We are no longer requiring the NCT logo instead under Lena Voss D.M.D. M.S. PC it should say; "Board Certified Orthodontist" Obviously this is without the quotations. Also the back side of the business card MUST include the remaining office locations. If your draft is submitted without this information on the back it WILL BE ELIMINATED!
*****PLEASE READ THE BRIEF BEFORE SUBMITTING DESIGNS AS THE NCT LOGO MUST BE INCLUDED******** We need all new office supplies as one of our doctors has retired. Business cards (front and back) Stationary (letterhead, envelopes #10, large flat envelopes 12"x15") Included in the brief is a copy of our current letterhead and business card (front & back) to be used as a base point. Our remaining doctor is young, professional, and very modern. Please let this be reflected in the designs that you present.

```html
<!DOCTYPE html>
<html lang="en">
<head>
<meta charset="utf-8">
<title>Lena Voss Orthodontics – Business Card</title>
<link rel="stylesheet" href="https://fonts.googleapis.com/css2?family=Open+Sans:wght@400;600&display=swap">
<style>
  :root {
    --backdrop: #2e2f31;
    --paper: #ffffff;
    --ink: #4a4d52;
    --ink-soft: #7a7e84;
    --brand-blue: #2c9fd9;
    --brand-blue-deep: #1b86c4;
    --brand-blue-light: #63bde9;
  }
  * { margin: 0; padding: 0; box-sizing: border-box; }
  html, body { width: 1200px; height: 969px; overflow: hidden; }
  body {
    background: var(--backdrop);
    font-family: "Open Sans", Arial, sans-serif;
    color: var(--ink);
    position: relative;
  }
  .card {
    position: absolute;
    left: 200px;
    width: 800px;
    height: 457px;
    background: var(--paper);
    overflow: hidden;
  }
  .card--back { top: 18px; }
  .card--front { top: 494px; }

  .brand {
    position: absolute;
    display: flex;
    align-items: center;
    gap: 12px;
  }
  .brand__dot {
    width: 52px; height: 52px;
    border-radius: 50%;
    background: var(--brand-blue);
    flex: none;
  }
  .brand__name {
    font-size: 24px;
    font-weight: 600;
    color: var(--brand-blue);
    letter-spacing: 0.4px;
    line-height: 1.1;
    white-space: nowrap;
  }
  .brand__tagline {
    font-size: 12px;
    color: var(--ink-soft);
    letter-spacing: 0.6px;
    margin-top: 4px;
    white-space: nowrap;
  }

  /* back side */
  .card--back .brand { left: 50px; top: 196px; }
  .locations {
    position: absolute;
    font-size: 13px;
    line-height: 1.5;
    color: var(--ink);
    white-space: nowrap;
  }
  .locations--main { left: 470px; top: 170px; }
  .locations--extra { left: 620px; top: 92px; }
  .locations__title { font-weight: 600; }
  .locations__office + .locations__office { margin-top: 8px; }

  /* front side */
  .card--front .brand { left: 48px; top: 48px; }
  .doctor {
    position: absolute;
    right: 58px;
    top: 120px;
    text-align: right;
  }
  .doctor__name { font-size: 24px; color: var(--ink); }
  .doctor__title { font-size: 14px; color: var(--ink-soft); letter-spacing: 0.5px; }
  .contact-band {
    position: absolute;
    left: 0; right: 0;
    top: 238px;
    height: 126px;
    background: linear-gradient(90deg, var(--brand-blue-deep), var(--brand-blue) 55%, var(--brand-blue-light));
  }
  .contact {
    position: absolute;
    left: 48px;
    top: 250px;
    color: #fff;
    font-size: 15px;
    line-height: 1.6;
  }
  .tooth-art {
    position: absolute;
    right: 90px;
    top: 188px;
    width: 130px;
    height: 160px;
    border-radius: 52px 52px 36px 36px;
    background: linear-gradient(180deg, rgba(255,255,255,0.9), rgba(44,159,217,0.35));
  }
  .board-badge {
    position: absolute;
    left: 48px;
    top: 384px;
    width: 44px;
    height: 44px;
    border-radius: 50%;
    background: var(--ink);
  }
</style>
</head>
<body>

  <section class="card card--back">
    <div class="brand">
      <span class="brand__dot"></span>
      <div>
        <p class="brand__name">Lena Voss Orthodontics</p>
        <p class="brand__tagline">Board Certified Orthodontist</p>
      </div>
    </div>
    <div class="locations locations--main">
      <p class="locations__title">Attica</p>
      <p>4712 W. Tarrow St.</p>
      <p>Attica, NY 14906</p>
      <p>(585)555-0126</p>
    </div>
    <div class="locations locations--extra">
      <p class="locations__title">Additional Locations:</p>
      <div class="locations__office">
        <p>Blasdell</p>
        <p>5193 Hollin Ridge Ave.</p>
        <p>Blasdell, NY 14387</p>
        <p>(716)555-0193</p>
      </div>
      <div class="locations__office">
        <p>Cheektowaga</p>
        <p>2615 Fenwick Rd.</p>
        <p>Cheektowaga, NY 14391</p>
        <p>(716)555-0147</p>
      </div>
      <div class="locations__office">
        <p>Warsaw</p>
        <p>58 Lorimer St.</p>
        <p>Warsaw, NY 14802</p>
        <p>(585)555-0126</p>
      </div>
    </div>
  </section>

  <section class="card card--front">
    <div class="brand">
      <span class="brand__dot"></span>
      <span class="brand__name">Lena Voss Orthodontics</span>
    </div>
    <div class="doctor">
      <p class="doctor__name">Lena Voss</p>
      <p class="doctor__title">D.M.D. M.S. PC</p>
    </div>
    <div class="contact-band"></div>
    <div class="tooth-art" role="img" aria-label="Outlined tooth illustration in brand blue"></div>
    <div class="contact">
      <p>4127 Marlow Ct Williamsville, NY 14398</p>
      <p>Tel: (716)555-0172 &nbsp;Fax: (716)555-0188</p>
      <p>Email: Info@SmileCraftClinics.com</p>
      <p>www.SmileCraftClinics.com</p>
    </div>
    <div class="board-badge" aria-hidden="true"></div>
  </section>

</body>
</html>
```